BRELM - Letterhead

Willowmere Institute of Letters and Crafts (BRELM) is a non-profit organization that operates two tuition-free public schools - BRELM Elementary for grades K to 5th and BRELM College Prep for grades 6-12.

We are looking for a letterhead primarily to be used on Google Docs and Microsoft Word. Attached are two versions of our logo. One with our name spelled out and one with the acronym.

For Letterhead, we would like 3 addresses listed:

BRELM HQ
41872 Hollow Brook Lane, Suite 308
Fernhaven, CA 90412

BRELM Elementary (K-5)
18460 Marsh Ridge Boulevard
Fernhaven, CA 90412

BRELM College Prep (6-12)
27314 Del Sol Terrace
Cedar Hollow, CA 90418

Our Phone Number is (555) 418-7062
Our Fax Number is the same (555) 418-7062

Our website is www.brelmschools.org

Target Market(s)

Education

Industry/Entity Type

Education

Font styles to use
Sans Serif

Colors
0054AA
0677BA
7BADD7
CADEEF
E8F1F8

Requirements
Must have
• Logo, Address, Phone Number, Website.
Nice to have
• Modern and clean design.
Should not have
• Prefer that there is no bleed -- the letterhead will mostly be used in PDF format however sometimes it will be printed and our printers can not do a full bleed

```html
<!DOCTYPE html>
<html lang="en">
<head>
<meta charset="utf-8">
<title>BRELM Letterhead</title>
<link href="https://fonts.googleapis.com/css2?family=Montserrat:wght@400;500;700&display=swap" rel="stylesheet">
<style>
  :root {
    --brand-blue: #2b4fa6;
    --deep-blue: #0054AA;
    --mid-blue: #0677BA;
    --soft-blue: #7BADD7;
    --pale-blue: #CADEEF;
    --text-gray: #6b6b6b;
    --ink: #333333;
    --paper: #ffffff;
    --backdrop: #d6d6d6;
  }
  * { box-sizing: border-box; margin: 0; padding: 0; }
  html, body { width: 1200px; height: 800px; overflow: hidden; }
  body {
    background: var(--backdrop);
    font-family: "Montserrat", sans-serif;
    display: flex;
    align-items: center;
    justify-content: center;
  }
  .letterhead {
    position: relative;
    width: 572px;
    height: 740px;
    background: var(--paper);
    box-shadow: 0 2px 10px rgba(0,0,0,0.12);
  }
  .contact {
    position: absolute;
    top: 52px;
    right: 52px;
    text-align: right;
    font-size: 7.5px;
    line-height: 1.5;
    color: var(--ink);
  }
  .contact .label {
    color: var(--brand-blue);
    font-weight: 700;
    font-size: 6.5px;
    letter-spacing: 0.02em;
    margin-right: 3px;
  }
  .brand {
    position: absolute;
    top: 118px;
    left: 52px;
    display: flex;
    align-items: center;
    gap: 10px;
  }
  .brand-mark {
    width: 26px;
    height: 26px;
    border-radius: 50%;
    background: var(--brand-blue);
  }
  .brand-name {
    color: var(--brand-blue);
    font-weight: 700;
    font-size: 13px;
    line-height: 1.15;
  }
  .letter-body {
    position: absolute;
    top: 222px;
    left: 92px;
    width: 400px;
    font-size: 8.5px;
    line-height: 1.65;
    color: var(--text-gray);
  }
  .letter-body p + p { margin-top: 12px; }
  .closing {
    position: absolute;
    top: 478px;
    right: 86px;
    width: 110px;
    text-align: center;
  }
  .closing .sign-off {
    font-size: 8px;
    color: var(--text-gray);
    margin-bottom: 6px;
  }
  .locations {
    position: absolute;
    left: 52px;
    right: 52px;
    bottom: 48px;
    display: flex;
    justify-content: space-between;
  }
  .location {
    width: 140px;
    border-top: 1.5px solid var(--brand-blue);
    padding-top: 8px;
    font-size: 7.5px;
    line-height: 1.5;
    color: var(--ink);
  }
  .location-name {
    color: var(--brand-blue);
    font-weight: 700;
  }
</style>
</head>
<body>
  <main class="letterhead">
    <div class="contact">
      <div><span class="label">PHONE / FAX</span>(555) 418-7062</div>
      <div><span class="label">WEB</span>www.brelmschools.org</div>
    </div>

    <div class="brand">
      <div class="brand-mark"></div>
      <div class="brand-name">Willowmere Institute<br>of Letters and Crafts</div>
    </div>

    <section class="letter-body">
      <p>Lorem ipsum dolor sit amet, consectetur adipiscing elit. Donec orci purus, luctus vitae dignissim eu, iaculis sed purus. Vivamus faucibus, ipsum nec aliquet viverra, leo mauris condimentum ligula, sit amet sagittis enim ligula quis arcu. Nam egestas tortor id nisl porttitor mattis. In tortor ante, ultricies in suscipit a, tempus non massa. Vivamus et auctor mi. Fusce vel massa nulla. Phasellus nec eros mauris, et scelerisque orci.</p>
      <p>Donec malesuada orci vitae nulla accumsan porta a id massa. Quisque accumsan iaculis magna sit amet fringilla. Maecenas consequat, magna eget tincidunt semper, odio nibh rutrum mi, id feugiat ante nisi eu risus. Vestibulum nunc orci, rhoncus a placerat in, ultricies in mi. Cras mattis varius eros, vel fringilla nisi suscipit eget. Quisque scelerisque sagittis nulla at porttitor.</p>
      <p>Sed id augue vitae urna euismod commodo aliquet a quam. Pellentesque arcu velit, cursus et malesuada ut, consequat et diam. Nullam erat sem, rhoncus id ullamcorper vitae, rhoncus et arcu. In ultricies ultricies nulla, ut rutrum nisi iaculis at. Donec eu magna a metus ornare faucibus. Fusce aliquet faucibus ultricies. Morbi semper, est id tincidunt gravida, sem arcu adipiscing lacus, ac bibendum nulla leo eu purus. Quisque nec diam sed risus consectetur accumsan quis quis nibh. Vestibulum id purus lorem.</p>
    </section>

    <div class="closing">
      <div class="sign-off">Sincerely,</div>
      <svg width="76" height="76" viewBox="0 0 76 76" aria-hidden="true">
        <circle cx="38" cy="38" r="35" fill="none" stroke="var(--soft-blue)" stroke-width="2"/>
        <circle cx="38" cy="38" r="24" fill="none" stroke="var(--soft-blue)" stroke-width="1"/>
      </svg>
    </div>

    <footer class="locations">
      <div class="location">
        <div class="location-name">BRELM HQ</div>
        <div>41872 Hollow Brook Lane, Suite 308</div>
        <div>Fernhaven, CA 90412</div>
      </div>
      <div class="location">
        <div class="location-name">BRELM Elementary (K-5)</div>
        <div>18460 Marsh Ridge Boulevard</div>
        <div>Fernhaven, CA 90412</div>
      </div>
      <div class="location">
        <div class="location-name">BRELM College Prep (6-12)</div>
        <div>27314 Del Sol Terrace</div>
        <div>Cedar Hollow, CA 90418</div>
      </div>
    </footer>
  </main>
</body>
</html>
```